Laptop Accessories Packing Design

We are looking for a new package design of a laptop accesories (batteries, charges, hard drives etc.). We want to refresh our brand Vireo CellWorks. At VireoCell, we create high-end laptop accessories that ensure reliability, performance, and longevity for users worldwide. Our mission is to deliver innovative and durable solutions that allow users to work, create, and grow without limits.
General Packaging Concept
Minimalist and elegant look, yet with elements that catch the eye (Vireo products will mainly be offered on auction portals such as Brindle, Kiva, Tollmart, so it would be good if the packaging attracted attention and stood out from the competitors).
Should I put a photo, sketch or product icon on the box? We'll leave that to your imagination.
We ask for a general design of the packaging. After the competition, together with the winner, we will add the rest of the information to the back and sides of the box.
In the attachments there is our Logo (you can use other colors) and sample packaging of competitors
Target Market(s)
E-commerse
Industry/Entity Type
individual end customer
Look and feel
Each slider illustrates characteristics of the customer's brand and the style your logo design should communicate.

```html
<!DOCTYPE html>
<html lang="en">
<head>
<meta charset="utf-8">
<title>Vireo CellWorks – Laptop Accessories Box Front</title>
<link rel="stylesheet" href="https://fonts.googleapis.com/css2?family=Poppins:wght@600;800&display=swap">
<style>
  :root {
    --page-bg: #f4f4f4;
    --panel-top: #4a4a4a;
    --panel-mid: #2b2b2b;
    --panel-bottom: #0d0d0d;
    --gold-dark: #b8772a;
    --gold-light: #d4b860;
    --gold-brand: #d9a43a;
    --emblem-top: rgba(150, 115, 70, 0.55);
    --emblem-bottom: rgba(90, 60, 25, 0.45);
    --text-light: #ececec;
    --edge-dark: #111111;
  }
  * { margin: 0; padding: 0; box-sizing: border-box; }
  html, body {
    width: 1200px;
    height: 969px;
    overflow: hidden;
    background: var(--page-bg);
  }
  .canvas {
    position: relative;
    width: 1200px;
    height: 969px;
  }
  .box-front {
    position: absolute;
    left: 170px;
    top: 245px;
    width: 860px;
    height: 480px;
    overflow: hidden;
    background: linear-gradient(165deg, var(--panel-top) 0%, var(--panel-mid) 45%, var(--panel-bottom) 100%);
    border-left: 22px solid var(--edge-dark);
  }
  .gold-band {
    position: absolute;
    left: 0;
    top: 0;
    width: 18px;
    height: 100%;
    background: linear-gradient(180deg, var(--gold-dark) 0%, var(--gold-light) 50%, var(--gold-dark) 100%);
  }
  .band-shadow {
    position: absolute;
    left: 18px;
    top: 0;
    width: 24px;
    height: 100%;
    background: var(--edge-dark);
  }
  .texture-area {
    position: absolute;
    right: 0;
    top: 0;
    width: 70%;
    height: 100%;
    background: linear-gradient(90deg, rgba(255,255,255,0) 0%, rgba(255,255,255,0.04) 60%, rgba(255,255,255,0.06) 100%);
  }
  .emblem-area {
    position: absolute;
    left: 42px;
    top: 0;
    width: 270px;
    height: 480px;
    border-radius: 0 60px 0 0;
    background: linear-gradient(180deg, var(--emblem-top) 0%, var(--emblem-bottom) 100%);
  }
  .brand-mark {
    position: absolute;
    right: 30px;
    top: 42px;
    display: flex;
    align-items: center;
    gap: 10px;
    font-family: 'Poppins', sans-serif;
    font-weight: 800;
    font-size: 32px;
    line-height: 1;
    color: var(--gold-brand);
  }
  .brand-dot {
    width: 12px;
    height: 12px;
    border-radius: 50%;
    background: var(--gold-brand);
  }
  .tagline {
    position: absolute;
    right: 34px;
    bottom: 50px;
    text-align: right;
    font-family: 'Poppins', sans-serif;
    font-weight: 600;
    font-size: 31px;
    line-height: 1.35;
    letter-spacing: 0.12em;
    color: var(--text-light);
  }
</style>
</head>
<body>
  <main class="canvas">
    <section class="box-front">
      <div class="gold-band"></div>
      <div class="band-shadow"></div>
      <div class="texture-area" role="img" aria-label="Subtle dark hexagon honeycomb texture"></div>
      <div class="emblem-area" role="img" aria-label="Large faint gold brand emblem decoration"></div>
      <div class="brand-mark">
        <span class="brand-dot"></span>
        <span class="brand-name">Vireo CellWorks</span>
      </div>
      <p class="tagline">HIGH END<br>LAPTOP ACCESORIES</p>
    </section>
  </main>
</body>
</html>
```